New Business Cards for Torvin Group

We need a new Business Card to compliment our new logo. We are a vibrant design, manufacture and install business providing recreation areas, public parks and Municipal spaces. We want business cards that are classy, modern and clean.

We have recently changed our logo, and are celebrating our 40th anniversary. We want business cards with a new modern design to reflect our status.

Target Market(s)

Customers

Contact Information for Business Card

We need all the details of our 3 offices as per the business card attached. Please disregard the old logo on the business card, the other three files show our new logo.

Requirements
Must have
• All info as per attached business card but with new logo.
Nice to have

```html
<!DOCTYPE html>
<html lang="en">
<head>
<meta charset="utf-8">
<title>Torvin Group – Business Card</title>
<link href="https://fonts.googleapis.com/css2?family=Lato:wght@400;700&display=swap" rel="stylesheet">
<style>
  :root {
    --red: #e8343b;
    --red-light: #f0585e;
    --ink: #1c1c1c;
    --grey: #6b6b6b;
    --paper: #ffffff;
    --paper-shade: #ececec;
    --black: #0d0d0d;
    --black-soft: #1e1e1e;
    --stage: #d9d6d2;
  }
  * { box-sizing: border-box; margin: 0; padding: 0; }
  html, body { width: 1200px; height: 900px; overflow: hidden; }
  body {
    background: var(--stage);
    font-family: "Lato", sans-serif;
    color: var(--ink);
    position: relative;
  }
  .card {
    position: absolute;
    left: 250px;
    width: 700px;
    height: 400px;
    overflow: hidden;
    box-shadow: 0 6px 18px rgba(0,0,0,0.25);
  }

  /* Back side */
  .card-back {
    top: 40px;
    background: linear-gradient(135deg, var(--black-soft) 0%, var(--black) 70%);
  }
  .card-back .world-map {
    position: absolute;
    inset: 40px 30px 60px 30px;
    background: radial-gradient(ellipse at 50% 50%, rgba(255,255,255,0.05) 0%, rgba(255,255,255,0.015) 60%, transparent 80%);
  }
  .card-back .brand {
    position: absolute;
    top: 140px;
    left: 0; right: 0;
    display: flex;
    justify-content: center;
    align-items: center;
    gap: 18px;
  }
  .brand-dot {
    width: 74px; height: 74px;
    border-radius: 50%;
    background: var(--red);
    flex: none;
  }
  .card-back .brand-name {
    font-size: 52px;
    font-weight: 700;
    color: #8a8a8a;
    letter-spacing: 1px;
  }
  .card-back .established {
    position: absolute;
    top: 262px;
    left: 0; right: 0;
    text-align: center;
    color: #e6e6e6;
    font-size: 16px;
  }
  .card-back .web {
    position: absolute;
    bottom: 48px;
    left: 0; right: 0;
    text-align: center;
    color: var(--red);
    font-size: 15px;
    letter-spacing: 4px;
  }

  /* Front side */
  .card-front {
    top: 460px;
    background: linear-gradient(180deg, var(--paper) 0%, var(--paper) 55%, var(--paper-shade) 100%);
  }
  .holder { position: absolute; top: 28px; left: 46px; }
  .holder-name { font-size: 34px; font-weight: 400; color: #333; line-height: 1.1; }
  .holder-role { font-size: 17px; color: var(--red); margin-top: 2px; }
  .holder-contact { margin-top: 16px; font-size: 16px; color: #333; }
  .contact-row { display: flex; align-items: center; gap: 12px; height: 26px; }
  .contact-row svg { flex: none; }

  .card-front .brand {
    position: absolute;
    top: 70px;
    right: 40px;
    display: flex;
    align-items: center;
    gap: 12px;
  }
  .card-front .brand-dot { width: 52px; height: 52px; }
  .card-front .brand-name {
    font-size: 30px;
    font-weight: 700;
    color: #555;
  }

  .offices {
    position: absolute;
    top: 186px;
    left: 46px;
    right: 30px;
    display: grid;
    grid-template-columns: 225px 218px 1fr;
  }
  .office { font-size: 15px; line-height: 22px; color: var(--ink); }
  .office-title { color: var(--red); font-size: 16px; }
  .office .label { color: var(--red); }

  .band {
    position: absolute;
    left: 0; right: 0; bottom: 0;
    height: 48px;
    background: linear-gradient(90deg, var(--red) 0%, var(--red-light) 100%);
    display: flex;
    align-items: center;
    justify-content: center;
    color: #fff;
    font-size: 17px;
    letter-spacing: 5px;
  }
</style>
</head>
<body>

<section class="card card-back">
  <div class="world-map" role="img" aria-label="Faint world map in the background"></div>
  <div class="brand">
    <span class="brand-dot"></span>
    <span class="brand-name">TORVIN GROUP</span>
  </div>
  <p class="established">Est. 1979</p>
  <p class="web">www.torvingroup.com</p>
</section>

<section class="card card-front">
  <div class="holder">
    <h1 class="holder-name">Marek Solenne</h1>
    <p class="holder-role">Managing Partner</p>
    <div class="holder-contact">
      <div class="contact-row">
        <svg width="14" height="20" viewBox="0 0 14 20" aria-hidden="true">
          <rect x="1.5" y="1" width="11" height="18" rx="2" fill="none" stroke="#e8343b" stroke-width="1.6"/>
          <line x1="5" y1="16" x2="9" y2="16" stroke="#e8343b" stroke-width="1.4"/>
        </svg>
        <span>+971 (0)50 384 7702</span>
      </div>
      <div class="contact-row">
        <svg width="20" height="14" viewBox="0 0 20 14" aria-hidden="true">
          <rect x="0" y="0" width="20" height="14" fill="#e8343b"/>
          <polyline points="0,0 10,8 20,0" fill="none" stroke="#fff" stroke-width="1.4"/>
        </svg>
        <span>marek@torvingroup.com</span>
      </div>
    </div>
  </div>

  <div class="brand">
    <span class="brand-dot"></span>
    <span class="brand-name">TORVIN GROUP</span>
  </div>

  <div class="offices">
    <div class="office">
      <p class="office-title">Head Office</p>
      <p>P.O. Box: 41820</p>
      <p>Abu Dhabi, U.A.E</p>
      <p><span class="label">T:</span> +971 (0)2 5530417</p>
      <p><span class="label">F:</span> +971 (0)2 5530418</p>
      <p><span class="label">E:</span> sales@torvingroup.com</p>
    </div>
    <div class="office">
      <p class="office-title">Dubai Office</p>
      <p>P.O. Box: 207315</p>
      <p>Dubai, U.A.E</p>
      <p><span class="label">T:</span> +971 (0)4 3862045</p>
      <p><span class="label">F:</span> +971 (0)4 3862046</p>
      <p><span class="label">E:</span> sales@torvingroup.com</p>
    </div>
    <div class="office">
      <p class="office-title">Qatar Office</p>
      <p>P.O. Box: 30982</p>
      <p>Doha, Qatar</p>
      <p><span class="label">T:</span> +974 55173308</p>
      <p><span class="label">F:</span> +974 55173308</p>
      <p><span class="label">E:</span> sales@torvingroup.com</p>
    </div>
  </div>

  <div class="band">www.torvingroup.com</div>
</section>

</body>
</html>
```